Personal Finance Blog Wordpress Design

We are looking for a new Wordpress theme design for CoinHarborly.com.

All of the elements that are currently on the homepage should remain, minus the archives list. The placement of various elements can be changed, we just need a more modern and clean feel. We would like to add a 160 x 600 ad unit on the homepage. We would like the 728x90 ad to be below the navigation similar to that of: http://www.plumtreeledger.org/blog/

We like the fonts used on: http://www.quillpocket.com/blog/

The text that currently resides at the bottom of CoinHarborly.com needs to remain on the homepage, but wherever it is placed needs to not be intrusive.

The color scheme needs to appropriately compliment the logo.

No sliders. I don't like sliders.

I am happy to answer questions.

Industry/Entity Type

Finance

Requirements
Must have
• Included in project description
Nice to have
Should not have
• Included in project description. Don't use sliders

```html
<!DOCTYPE html>
<html lang="en">
<head>
<meta charset="utf-8">
<title>CoinHarborly – Personal Finance Blog</title>
<link href="https://fonts.googleapis.com/css2?family=Lora:wght@400;700&family=Open+Sans:wght@400;600;700&display=swap" rel="stylesheet">
<style>
:root{
  --green:#8cc21f;
  --green-dark:#2f7a16;
  --green-label:#7cb518;
  --ink:#222;
  --muted:#555;
  --line:#d8d8d8;
  --panel:#f1f1f1;
  --page:#fff;
  --meta:#7cb518;
  --link:#2a7fc9;
}
*{box-sizing:border-box;margin:0;padding:0}
html,body{width:1200px;height:3600px;overflow:hidden;background:var(--page);font-family:"Open Sans",sans-serif;color:var(--ink)}
.page{position:relative;width:1200px;height:3600px}
.abs{position:absolute}
.brand{left:100px;top:10px;display:flex;align-items:center;gap:8px;font-weight:700;font-size:22px;color:var(--green-dark)}
.brand .dot{width:26px;height:26px;border-radius:50%;background:var(--green)}
.nav{left:0;top:52px;width:1200px;height:26px;background:var(--green-dark);display:flex;justify-content:center;gap:40px;align-items:center}
.nav a{color:#fff;font-family:Lora,serif;font-size:15px;text-decoration:none}
.leader{left:288px;top:92px;width:624px;height:86px;border:1px solid #ccc;background:#fff;padding:8px 14px}
.leader h3{color:#1a5fc9;font-size:30px;font-weight:600}
.leader p{font-size:13px;color:#333}
.leader .go{position:absolute;right:22px;top:14px;width:60px;height:52px;background:#3ba84a;border-radius:6px;display:flex;align-items:center;justify-content:center}
.hero-img{left:96px;top:192px;width:715px;height:312px;background:radial-gradient(ellipse at 50% 40%,#e9e2d2 0,#c9b69f 30%,#9c7f69 65%,#6f5a4d)}
.hero-box{left:96px;top:504px;width:715px;height:228px;background:var(--green);padding:20px 30px;color:#fff}
.hero-box h1{font-family:Lora,serif;font-size:27px;font-weight:700}
.hero-box .meta{display:flex;justify-content:space-between;font-size:14px;margin:22px 0 14px}
.hero-box p{font-size:14px;line-height:1.5}
.btn{display:inline-block;margin-top:12px;background:#f29a1d;color:#fff;font-family:Lora,serif;font-size:15px;padding:8px 20px}
.grid{left:96px;top:752px;width:715px;height:340px;display:grid;grid-template-columns:1fr 1fr;grid-template-rows:1fr 1fr}
.card{display:flex;gap:12px;padding:12px 8px;border-bottom:1px solid var(--line)}
.card:nth-child(odd){border-right:1px solid var(--line)}
.thumb{flex:none}
.card .thumb{width:70px;height:60px}
.card h4{font-family:Lora,serif;font-size:15px;line-height:1.35}
.meta-s{font-size:12px;color:var(--meta);margin:8px 0}
.card p{font-size:12.5px;color:var(--muted);line-height:1.5}
.sec{left:96px;width:715px;height:283px}
.sec .label{font-family:Lora,serif;font-weight:700;color:var(--green-label);font-size:19px;letter-spacing:.5px;height:36px;border-bottom:2px solid var(--line);padding-left:20px}
.sec .body{display:flex;gap:24px;padding:16px 0 0 18px}
.sec .thumb{width:110px;height:90px;margin-top:14px}
.sec h2{font-family:Lora,serif;font-size:21px;font-weight:700;line-height:1.4}
.sec .meta-s{font-size:13px;margin:10px 0}
.sec p{font-size:16px;line-height:1.55;color:#333;width:540px}
.sec .more{font-size:13px;font-weight:700;margin-top:10px}
.side{left:828px;width:276px;background:var(--panel)}
.widget-head{height:40px;background:var(--green);color:#fff;font-family:Lora,serif;font-weight:700;font-size:17px;display:flex;align-items:center;gap:10px;padding-left:14px}
.search{margin:16px 14px;height:26px;background:#fff;border:1px solid #ccc;font-size:12px;padding:4px 8px;color:#777}
.socials{display:flex;gap:14px;justify-content:center;margin-top:22px}
.socials span{width:30px;height:30px;border-radius:50%;background:var(--green-dark);display:flex;align-items:center;justify-content:center}
.post{display:flex;gap:10px;padding:12px 14px;height:173px;border-bottom:1px solid #ddd;background:#fff;margin:0 4px}
.post .thumb{width:48px;height:48px;background:linear-gradient(160deg,#e4e6ea,#b9a79a 60%,#5d5752)}
.post h5{font-family:Lora,serif;font-size:16px;line-height:1.3;font-weight:400}
.post p{font-size:12.5px;line-height:1.55;color:#444;margin-top:6px}
.post .foot{display:flex;justify-content:space-between;align-items:center;margin-top:12px;font-size:11px;color:var(--meta)}
.dots{display:flex;gap:3px}
.dots i{width:9px;height:9px;border-radius:50%;display:block}
.news{padding:14px;font-size:12px;line-height:1.5}
.news .in{height:26px;background:#fff;border:1px solid #ccc;margin:12px 0 6px;padding:4px 8px;color:#777}
.news .sub{height:24px;background:var(--green-dark);color:#fff;text-align:center;font-size:12px;line-height:24px;font-weight:600}
.sky{left:828px;top:1836px;width:276px;height:228px;background:linear-gradient(120deg,#e2b57f,#a8683f 45%,#c58a4f 70%,#4b7ab4)}
.sky-card{position:absolute;right:12px;top:8px;width:106px;height:210px;background:#fff;padding:10px;text-align:center;font-size:10px}
.sky-card .round{display:block;width:40px;height:40px;border-radius:50%;background:#2c9b45;margin:4px auto 0}
.sky-card b{display:block;color:#2c9b45;font-size:14px;margin:8px 0 6px}
.sky-card span{display:inline-block;margin-top:8px;border:1px solid #2c9b45;color:#2c9b45;padding:3px 6px}
.tweet{display:flex;gap:8px;background:#fff;margin:6px 10px;padding:8px;font-size:10.5px;line-height:1.5;height:90px;border-bottom:1px solid #ddd}
.tweet .thumb{width:34px;height:34px;background:linear-gradient(135deg,#cfd8e3,#8f9cab)}
.tweet em{color:var(--link);font-style:normal;text-decoration:underline}
.fb{left:828px;top:2621px;width:276px;height:326px;border:1px solid #ccc;background:#fff;padding:12px}
.fb .top{display:flex;align-items:center;justify-content:space-between;font-weight:700;color:var(--green-dark);font-size:15px}
.fb .like{width:50px;height:20px;background:#3b5998;color:#fff;font-size:11px;text-align:center;line-height:20px;font-weight:600}
.faces{display:grid;grid-template-columns:repeat(5,42px);gap:8px;margin-top:14px}
.faces span{height:42px}
.about{left:120px;top:3398px;width:960px}
.about h3{font-family:Lora,serif;font-size:19px;font-weight:700}
.about p{font-size:7.4px;line-height:1.6;margin-top:12px;color:#333}
.footer{left:0;top:3548px;width:1200px;height:52px;background:var(--green-dark);color:#fff;font-size:13px;display:flex;justify-content:center;align-items:center;gap:14px}
</style>
</head>
<body>
<div class="page">
  <div class="abs brand"><span class="dot"></span>CoinHarborly</div>
  <nav class="abs nav">
    <a>Auto</a><a>Bank Accounts</a><a>Credit Cards</a><a>Insurance</a><a>Investments</a><a>Mortgages</a><a>Personal Finance</a><a>Small Business</a><a>Taxes</a>
  </nav>
  <div class="abs leader"><h3>TradeNova - your best choice</h3><p>Market execution, no requotes Fast withdrawal, bonuses, contests!</p><div class="go"><svg width="22" height="22" viewBox="0 0 22 22"><path d="M8 4l7 7-7 7" fill="none" stroke="#fff" stroke-width="3"/></svg></div></div>

  <div class="abs hero-img" role="img" aria-label="Photo of hands holding up a one dollar bill"></div>
  <div class="abs hero-box">
    <h1>5 Easy Ways for Teenagers to Make a Lot of Money</h1>
    <div class="meta"><span>May 1st, 2015 · 0 Comment</span><span>5 Comments</span></div>
    <p>Want to make some money this summer or in the after-school hours, but you're not into the idea of flipping burgers, bagging groceries....</p>
    <span class="btn">Read More</span>
  </div>

  <div class="abs grid">
    <div class="card"><div class="thumb" style="background:linear-gradient(135deg,#f4f7fb,#cdd9ea)" role="img" aria-label="HomeTrail brand thumbnail"></div><div><h4>HomeTrail Financing: How it Helps to Prevent Foreclosure</h4><div class="meta-s">Apr 30th, 2015 · 0 Comment</div><p>The housing market is one of the most important indicators of the...</p></div></div>
    <div class="card"><div class="thumb" style="background:linear-gradient(135deg,#7ab3e0,#f1c24b 50%,#e06c5a)" role="img" aria-label="Coupon app icons on a phone"></div><div><h4>Best Coupon Apps for the Frugal Mom</h4><div class="meta-s">Apr 30th, 2015 · 0 Comment</div><p>It can be hard to justify the high price tag on a smartphone, let...</p></div></div>
    <div class="card"><div class="thumb" style="background:linear-gradient(135deg,#f3f3f3,#d9342b 55%,#f3f3f3)" role="img" aria-label="Home for sale sign"></div><div><h4>Important Tips About Short Sales Every Home Buyer Should</h4><div class="meta-s">Apr 30th, 2015 · 0 Comment</div><p>You have tried loan modification and a forbearance agreement, and...</p></div></div>
    <div class="card"><div class="thumb" style="background:linear-gradient(135deg,#efe9dc,#b8a27e)" role="img" aria-label="Work from home notice"></div><div><h4>Real Work from Home Jobs: Fact or Fiction?</h4><div class="meta-s">Apr 30th, 2015 · 0 Comment</div><p>If you've done any hoofing around searching for legitimate work...</p></div></div>
  </div>

  <section class="abs sec" style="top:1122px"><div class="label">AUTO</div><div class="body"><div class="thumb" style="background:linear-gradient(180deg,#fff 20%,#d2282e 20%,#d2282e 60%,#1f4f9c 60%,#1f4f9c 75%,#fff 75%)" role="img" aria-label="Bulkway car buying program thumbnail"></div><div><h2>Car Shopping on a Budget? Bulkway Car Buying Is a Great Option</h2><div class="meta-s">Apr 29th, 2015 · 0 Comment</div><p>Many consumers are currently searching for a reliable new or used vehicle, and want to make sure they get the best deal. Some people need a vehicle so...</p><div class="more">More &gt;&gt;</div></div></div></section>
  <section class="abs sec" style="top:1405px"><div class="label">BANK ACCOUNTS</div><div class="body"><div class="thumb" style="background:linear-gradient(160deg,#fafafa 40%,#c9362d 60%,#e9e2dc)" role="img" aria-label="Rising savings chart illustration"></div><div><h2>Want to Increase Your Savings? Check Out These Great Saving Money Tips</h2><div class="meta-s">Apr 29th, 2015 · 0 Comment</div><p>Increasing the amount of money in a savings account is a goal shared by many people all over the country. In the United States, the national savings rate...</p><div class="more">More &gt;&gt;</div></div></div></section>
  <section class="abs sec" style="top:1688px"><div class="label">CREDIT CARDS</div><div class="body"><div class="thumb" style="background:radial-gradient(ellipse at 40% 50%,#a9a49c,#4a4641)" role="img" aria-label="Vantage card sign thumbnail"></div><div><h2>Benefits of a Vantage It Card</h2><div class="meta-s">Apr 29th, 2015 · 0 Comment</div><p>The Vantage company was founded by a retail group in 1985, and the company started offering the Vantage card to the consumers shortly after it came into...</p><div class="more">More &gt;&gt;</div></div></div></section>
  <section class="abs sec" style="top:1971px"><div class="label">INSURANCE</div><div class="body"><div class="thumb" style="background:linear-gradient(160deg,#fafafa 40%,#c9362d 60%,#e9e2dc)" role="img" aria-label="Rising chart illustration"></div><div><h2>What is the Best Dental Insurance for Seniors?</h2><div class="meta-s">Apr 29th, 2015 · 0 Comment</div><p>No matter what your age, your dental health should be a top priority in your life. While it may be easy to forgo dental care, things can take a turn for...</p><div class="more">More &gt;&gt;</div></div></div></section>
  <section class="abs sec" style="top:2254px"><div class="label">INVESTMENTS</div><div class="body"><div class="thumb" style="background:radial-gradient(ellipse at 50% 50%,#3d7ed6,#0c2a66)" role="img" aria-label="Orbitune Radio thumbnail"></div><div><h2>Orbitune Radio Stock: How it Fares in 2015</h2><div class="meta-s">Apr 29th, 2015 · 0 Comment</div><p>As the days of satellite radio seem to be numbered, there seems to be more interest on the shares of industry leader Orbitune Radio than on the company itself....</p><div class="more">More &gt;&gt;</div></div></div></section>
  <section class="abs sec" style="top:2537px"><div class="label">MORTGAGES</div><div class="body"><div class="thumb" style="background:linear-gradient(135deg,#f4f7fb,#cdd9ea)" role="img" aria-label="HomeTrail brand thumbnail"></div><div><h2>HomeTrail Financing: How it Helps to Prevent Foreclosure</h2><div class="meta-s">Apr 29th, 2015 · 0 Comment</div><p>The housing market is one of the most important indicators of the economy in the United States. There are many people that owned houses before the real...</p><div class="more">More &gt;&gt;</div></div></div></section>
  <section class="abs sec" style="top:2820px"><div class="label">PERSONAL FINANCE</div><div class="body"><div class="thumb" style="background:linear-gradient(180deg,#f6efe6 30%,#c98a4a 55%,#8a5a32)" role="img" aria-label="Teenager holding a sign"></div><div><h2>5 Easy Ways for Teenagers to Make a Lot of Money</h2><div class="meta-s">Apr 29th, 2015 · 0 Comment</div><p>Want to make some money this summer or in the after-school hours, but you're not into the idea of flipping burgers, bagging groceries, or working...</p><div class="more">More &gt;&gt;</div></div></div></section>
  <section class="abs sec" style="top:3103px"><div class="label">SMALL BUSINESS</div><div class="body"><svg class="thumb" width="110" height="90" viewBox="0 0 110 90" role="img" aria-label="Budget report with pie chart"><rect width="110" height="90" fill="#fafafa" stroke="#ddd"/><circle cx="40" cy="50" r="26" fill="#3f6fb6"/><path d="M40 50V24a26 26 0 0 1 24 16z" fill="#7cb518"/><path d="M40 50l24-10a26 26 0 0 1-6 28z" fill="#d54b3d"/><rect x="74" y="30" width="26" height="4" fill="#ccc"/><rect x="74" y="40" width="22" height="4" fill="#ccc"/><rect x="74" y="50" width="26" height="4" fill="#ccc"/></svg><div><h2>Best Budgeting Software for 2015</h2><div class="meta-s">Apr 29th, 2015 · 0 Comment</div><p>As businesses everywhere look to find new and more efficient ways to develop their budgets in 2015, much of their attention is focused on finding the best...</p><div class="more">More &gt;&gt;</div></div></div></section>

  <aside class="abs side" style="top:192px;height:180px">
    <div class="widget-head"><svg width="18" height="18" viewBox="0 0 18 18"><circle cx="7" cy="7" r="5" fill="none" stroke="#fff" stroke-width="2"/><path d="M11 11l5 5" stroke="#fff" stroke-width="2.5"/></svg>Search CoinHarborly</div>
    <div class="search">Search</div>
    <div class="socials">
      <span><svg width="16" height="16" viewBox="0 0 16 16"><rect x="2" y="4" width="12" height="9" fill="none" stroke="#fff" stroke-width="1.5"/><path d="M2 4l6 5 6-5" fill="none" stroke="#fff" stroke-width="1.5"/></svg></span>
      <span><svg width="16" height="16" viewBox="0 0 16 16"><path d="M8 2a4 4 0 0 1 4 4c0 3-4 8-4 8S4 9 4 6a4 4 0 0 1 4-4z" fill="#fff"/></svg></span>
      <span><svg width="16" height="16" viewBox="0 0 16 16"><path d="M3 8l3 3 7-7" fill="none" stroke="#fff" stroke-width="2"/></svg></span>
      <span><svg width="16" height="16" viewBox="0 0 16 16"><path d="M2 8h10M8 4l4 4-4 4" fill="none" stroke="#fff" stroke-width="2"/></svg></span>
      <span><svg width="16" height="16" viewBox="0 0 16 16"><path d="M2 8l6-5 6 5M4 7v6h8V7" fill="none" stroke="#fff" stroke-width="1.6"/></svg></span>
    </div>
  </aside>

  <aside class="abs side" style="top:379px;height:1243px">
    <div class="widget-head"><svg width="18" height="18" viewBox="0 0 18 18"><rect x="2" y="2" width="14" height="14" fill="none" stroke="#fff" stroke-width="2"/><path d="M5 7h8M5 11h8" stroke="#fff" stroke-width="1.5"/></svg>Recent Posts</div>
    <div class="post"><div class="thumb" role="img" aria-label="Author thumbnail"></div><div><h5>Lorem Ipsum is simply dummy text</h5><p>Lorem Ipsum is simply dummy text of the printing and typesetting industry</p><div class="foot"><span>2 days ago</span><span class="dots"><i style="background:#3b5998"></i><i style="background:#2aa3ef"></i><i style="background:#1b6fb5"></i><i style="background:#d54b3d"></i></span></div></div></div>
    <div class="post"><div class="thumb" role="img" aria-label="Author thumbnail"></div><div><h5>Lorem Ipsum is simply dummy text</h5><p>Lorem Ipsum is simply dummy text of the printing and typesetting industry</p><div class="foot"><span>2 days ago</span><span class="dots"><i style="background:#3b5998"></i><i style="background:#2aa3ef"></i><i style="background:#1b6fb5"></i><i style="background:#d54b3d"></i></span></div></div></div>
    <div class="post"><div class="thumb" role="img" aria-label="Author thumbnail"></div><div><h5>Lorem Ipsum is simply dummy text</h5><p>Lorem Ipsum is simply dummy text of the printing and typesetting industry</p><div class="foot"><span>2 days ago</span><span class="dots"><i style="background:#3b5998"></i><i style="background:#2aa3ef"></i><i style="background:#1b6fb5"></i><i style="background:#d54b3d"></i></span></div></div></div>
    <div class="post"><div class="thumb" role="img" aria-label="Author thumbnail"></div><div><h5>Lorem Ipsum is simply dummy text</h5><p>Lorem Ipsum is simply dummy text of the printing and typesetting industry</p><div class="foot"><span>2 days ago</span><span class="dots"><i style="background:#3b5998"></i><i style="background:#2aa3ef"></i><i style="background:#1b6fb5"></i><i style="background:#d54b3d"></i></span></div></div></div>
    <div class="post"><div class="thumb" role="img" aria-label="Author thumbnail"></div><div><h5>Lorem Ipsum is simply dummy text</h5><p>Lorem Ipsum is simply dummy text of the printing and typesetting industry</p><div class="foot"><span>2 days ago</span><span class="dots"><i style="background:#3b5998"></i><i style="background:#2aa3ef"></i><i style="background:#1b6fb5"></i><i style="background:#d54b3d"></i></span></div></div></div>
    <div class="post"><div class="thumb" role="img" aria-label="Author thumbnail"></div><div><h5>Lorem Ipsum is simply dummy text</h5><p>Lorem Ipsum is simply dummy text of the printing and typesetting industry</p><div class="foot"><span>2 days ago</span><span class="dots"><i style="background:#3b5998"></i><i style="background:#2aa3ef"></i><i style="background:#1b6fb5"></i><i style="background:#d54b3d"></i></span></div></div></div>
    <div class="post"><div class="thumb" role="img" aria-label="Author thumbnail"></div><div><h5>Lorem Ipsum is simply dummy text</h5><p>Lorem Ipsum is simply dummy text of the printing and typesetting industry</p><div class="foot"><span>2 days ago</span><span class="dots"><i style="background:#3b5998"></i><i style="background:#2aa3ef"></i><i style="background:#1b6fb5"></i><i style="background:#d54b3d"></i></span></div></div></div>
  </aside>

  <aside class="abs side" style="top:1639px;height:173px">
    <div class="widget-head"><svg width="18" height="18" viewBox="0 0 18 18"><rect x="1" y="4" width="16" height="11" fill="none" stroke="#fff" stroke-width="2"/><path d="M1 4l8 6 8-6" fill="none" stroke="#fff" stroke-width="2"/></svg>E-mail Newsletter</div>
    <div class="news">Sign up now to receive breaking news and to hear what's new with our website!<div class="in">Enter Your Email</div><div class="sub">Submit</div></div>
  </aside>

  <div class="abs sky" role="img" aria-label="Sidebar advertisement photo"><div class="sky-card"><i class="round"></i><b>ChatPeer</b>Get chat numbers from women near you<br><span>Get numbers</span></div></div>

  <aside class="abs side" style="top:2083px;height:521px">
    <div class="widget-head"><svg width="18" height="18" viewBox="0 0 18 18"><path d="M2 4h14v8H8l-4 4v-4H2z" fill="#fff"/></svg>Follow us</div>
    <div class="tweet"><div class="thumb" role="img" aria-label="Account avatar"></div><div>Lorem <em>@ipsum</em> dolor sit amet consectet adipisicing <em>@elit sed do</em> eiusmod tempor <em>@incididunt ut labore</em> et dolore</div></div>
    <div class="tweet"><div class="thumb" role="img" aria-label="Account avatar"></div><div>Lorem <em>@ipsum</em> dolor sit amet consectet adipisicing <em>@elit sed do</em> eiusmod tempor <em>@incididunt ut labore</em> et dolore</div></div>
    <div class="tweet"><div class="thumb" role="img" aria-label="Account avatar"></div><div>Lorem <em>@ipsum</em> dolor sit amet consectet adipisicing <em>@elit sed do</em> eiusmod tempor <em>@incididunt ut labore</em> et dolore</div></div>
    <div class="tweet"><div class="thumb" role="img" aria-label="Account avatar"></div><div>Lorem <em>@ipsum</em> dolor sit amet consectet adipisicing <em>@elit sed do</em> eiusmod tempor <em>@incididunt ut labore</em> et dolore</div></div>
    <div style="text-align:right;font-size:10px;color:var(--link);padding:6px 12px">Tweet To @CoinHarborly</div>
  </aside>

  <div class="abs fb">
    <div class="top"><span>CoinHarborly</span><span class="like">Like</span></div>
    <div style="font-size:11px;margin-top:10px">842 people like this</div>
    <div class="faces" role="img" aria-label="Grid of follower avatars">
      <span style="background:#8c7a6b"></span><span style="background:#4f5b6a"></span><span style="background:#b59a80"></span><span style="background:#3d3d3d"></span><span style="background:#9aa7b5"></span>
      <span style="background:#6b5646"></span><span style="background:#a68b6e"></span><span style="background:#556b4f"></span><span style="background:#c2a68d"></span><span style="background:#474c56"></span>
      <span style="background:#7d8a97"></span><span style="background:#5a4a3f"></span><span style="background:#b9a08a"></span><span style="background:#3f4a5c"></span><span style="background:#8f7965"></span>
    </div>
    <div style="font-size:10px;color:#777;margin-top:10px">Social page plugin</div>
  </div>

  <div class="abs about">
    <h3>Coin Harborly: Personal Finance Blog</h3>
    <p>Our mission is to make the lives of our readers financially easier by offering clear, practical personal finance content on the internet. Our readers are at many different stages in life, with different financial situations and needs. One person may be looking to get their first credit card, another may be looking for how to get a mortgage or buy a home, and some may be looking for ways to afford a college education for their children. Many want to know how to improve their credit score, and still others might be planning for retirement. Whatever your goal, we cover saving, borrowing, budgeting and building a steady family budget. Because there are so many different areas of banking and finance, we aim to share helpful tips and advice through our many articles. We hope you find useful ideas here, and we welcome you to share your own experiences with our community through the comments on each article.</p>
  </div>

  <footer class="abs footer"><span>© 2015 Coin Harborly. All rights reserved.</span><span>|</span><span>Contact Us</span><span>|</span><span>Privacy Policy</span><span>|</span><span>Terms and Conditions</span></footer>
</div>
</body>
</html>
```